Lantern Hearthworks Business Cards

Looking to create simple business cards that highlight our unique three sided triangle fire pit design with the colors and font of our logo, listed below.

Requirements
Must have
• Looking for something simple that includes a picture of our fire pit with name, website (lanternhearthworks.com), phone number and email. Want to keep the color mostly orange and black.
• Font is gotham(medium) and orange color code is #ee6e22

```html
<!DOCTYPE html>
<html lang="en">
<head>
<meta charset="utf-8">
<title>Lantern Hearthworks Business Cards</title>
<link rel="stylesheet" href="https://fonts.googleapis.com/css2?family=Montserrat:wght@500;600&family=Work+Sans:wght@400&display=swap">
<style>
  :root {
    --orange: #ee6e22;
    --ink: #3d3d3f;
    --slate: #6d6e70;
    --slate-deep: #5a5b5d;
    --paper: #ffffff;
    --backdrop: #262626;
  }
  * { margin: 0; padding: 0; box-sizing: border-box; }
  html, body { width: 1200px; height: 878px; overflow: hidden; }
  body { background: var(--backdrop); position: relative; }

  .card {
    position: absolute;
    left: 260px;
    width: 680px;
    height: 389px;
    overflow: hidden;
  }

  /* Back side */
  .card--back { top: 30px; background: var(--slate); }
  .back-wordmark {
    position: absolute;
    inset: 0;
    display: flex;
    align-items: center;
    justify-content: center;
    gap: 18px;
  }
  .back-wordmark__dot {
    width: 22px; height: 22px; border-radius: 50%;
    background: var(--slate-deep);
  }
  .back-wordmark__name {
    font-family: "Montserrat", sans-serif;
    font-weight: 500;
    font-size: 30px;
    letter-spacing: 4px;
    text-transform: uppercase;
    color: var(--slate-deep);
  }

  /* Front side */
  .card--front { top: 459px; background: var(--paper); }
  .front-wordmark {
    position: absolute;
    left: 36px;
    top: 140px;
    width: 266px;
    display: flex;
    align-items: center;
    gap: 12px;
  }
  .front-wordmark__dot {
    flex: none;
    width: 18px; height: 18px; border-radius: 50%;
    background: var(--orange);
  }
  .front-wordmark__name {
    font-family: "Montserrat", sans-serif;
    font-weight: 500;
    font-size: 23px;
    line-height: 1.2;
    letter-spacing: 3px;
    text-transform: uppercase;
    color: var(--orange);
  }
  .divider {
    position: absolute;
    left: 318px;
    top: 112px;
    width: 2px;
    height: 138px;
    background: var(--orange);
  }
  .contact {
    position: absolute;
    left: 340px;
    top: 112px;
    width: 320px;
  }
  .contact__name {
    font-family: "Montserrat", sans-serif;
    font-weight: 600;
    font-size: 28px;
    color: var(--orange);
    text-transform: uppercase;
    letter-spacing: 0.5px;
    white-space: nowrap;
  }
  .contact__role {
    font-family: "Work Sans", sans-serif;
    font-size: 15px;
    color: var(--ink);
    letter-spacing: 1px;
    margin-bottom: 14px;
  }
  .contact__line {
    display: flex;
    align-items: center;
    gap: 10px;
    font-family: "Work Sans", sans-serif;
    font-size: 16px;
    color: var(--ink);
    letter-spacing: 0.4px;
    line-height: 1.6;
    white-space: nowrap;
  }
  .contact__icon { width: 13px; height: 13px; flex: none; }
  .bands { position: absolute; left: 0; bottom: 0; width: 680px; height: 90px; }
</style>
</head>
<body>
  <section class="card card--back" aria-label="Card back">
    <div class="back-wordmark">
      <span class="back-wordmark__dot"></span>
      <span class="back-wordmark__name">Lantern Hearthworks</span>
    </div>
  </section>

  <section class="card card--front" aria-label="Card front">
    <div class="front-wordmark">
      <span class="front-wordmark__dot"></span>
      <span class="front-wordmark__name">Lantern Hearthworks</span>
    </div>

    <div class="divider"></div>

    <div class="contact">
      <p class="contact__name">Dane Holloway</p>
      <p class="contact__role">CO-Founder</p>
      <p class="contact__line">
        <svg class="contact__icon" viewBox="0 0 16 16"><path d="M4 1l3 3-2 2c1 2 3 4 5 5l2-2 3 3-2 3C7 15 1 9 1 3z" fill="none" stroke="#ee6e22" stroke-width="1.6"/></svg>
        555-014-2273
      </p>
      <p class="contact__line">
        <svg class="contact__icon" viewBox="0 0 16 16"><rect x="1" y="3" width="14" height="10" fill="none" stroke="#ee6e22" stroke-width="1.6"/><path d="M1 3l7 6 7-6" fill="none" stroke="#ee6e22" stroke-width="1.6"/></svg>
        hello@lanternhearthworks.com
      </p>
      <p class="contact__line">
        <svg class="contact__icon" viewBox="0 0 16 16"><circle cx="8" cy="8" r="7" fill="none" stroke="#ee6e22" stroke-width="1.5"/><path d="M1 8h14M8 1c-3 4-3 10 0 14M8 1c3 4 3 10 0 14" fill="none" stroke="#ee6e22" stroke-width="1.2"/></svg>
        www.lanternhearthworks.com
      </p>
    </div>

    <svg class="bands" viewBox="0 0 680 90" aria-hidden="true">
      <polygon points="0,30 318,30 300,52 0,52" fill="#6d6e70"/>
      <polygon points="326,52 680,52 680,70 308,70" fill="#ee6e22"/>
    </svg>
  </section>
</body>
</html>
```